Criminal Defense law firm needs website and logo

Need a logo design and web design for a small firm in Miami, Florida. The firm concentrates in the areas of state and federal criminal defense in Miami Dade County, Florida.The firm handles cases in the areas of Drug Possession, Fraud Offenses, Traffic Offenses, domestic violence, Violent Crimes, probation violation, Juvenile Delinquency, and expunction/expungment of criminal records (detailed list provided in attachment). The name of the attorney is Loreta Benavides-Kurtz. Sole Practitioner. Will attach profile. (the attachment are from my previous law firm, can use any of the language but adjust to a sole practitioner)

Industry/Entity Type

Lawyer

Number of Pages Required

3 page

Font styles to use
Serif

Colors
0356a4

Requirements
Must have
• Page that includes area's of practice. Page for Attorney profile. Contact page indicating that we speak Spanish and accept all major credit cards.

```html
<!DOCTYPE html>
<html lang="en">
<head>
<meta charset="utf-8">
<title>Benavides Kurtz Law — Criminal Defence</title>
<link rel="stylesheet" href="https://fonts.googleapis.com/css2?family=Open+Sans:wght@400;600;700&family=Raleway:wght@400;500;600&display=swap">
<style>
:root{
  --brand:#0356a4;
  --brand-dark:#034a8e;
  --brand-soft:#3a64a8;
  --ink:#333;
  --muted:#666;
  --line:#e3e3e3;
  --panel:#f4f4f4;
  --bar:#2f2f2f;
  --white:#fff;
}
*{box-sizing:border-box;margin:0;padding:0}
html,body{width:1200px;height:2267px;overflow:hidden}
body{position:relative;background:var(--white);font-family:"Open Sans",Arial,sans-serif;color:var(--ink)}
.abs{position:absolute}
.head{font-family:"Raleway",Helvetica,sans-serif}

/* top bar */
.topbar{left:0;top:0;width:1200px;height:30px;background:var(--brand);color:var(--white);font-size:12px}
.topbar .item{top:8px;display:flex;align-items:center;gap:8px}
.topbar .sq{width:12px;height:12px;background:var(--white);border-radius:2px;top:9px}

/* header */
.header{left:0;top:30px;width:1200px;height:96px;background:var(--white);border-bottom:1px solid #ddd}
.brand-name{left:97px;top:22px;color:var(--brand);font-family:"Raleway",sans-serif;font-weight:600;line-height:1}
.brand-name .l1{font-size:32px;letter-spacing:1px;display:block}
.brand-name .l2{font-size:17px;letter-spacing:2px;display:block;margin-top:3px}
.nav a{position:absolute;top:41px;font-size:13px;color:#222;text-decoration:none;letter-spacing:.3px}
.nav .active::after{content:"";position:absolute;left:0;right:0;top:54px;height:3px;background:var(--brand)}
.lang{left:988px;top:33px;width:112px;height:32px;border:1px solid #ddd;border-radius:3px;font-size:10px;color:#666;display:flex;align-items:center;padding-left:10px;gap:6px}
.lang .flag{width:14px;height:9px;background:#c4343f;border:2px solid #1f3c86}

/* hero */
.hero{left:0;top:126px;width:1200px;height:534px;background:linear-gradient(180deg,#8c8ec4 0%,#c2a9d4 30%,#d8c6dc 48%,#6a7c9e 66%,#2b3e5c 82%,#435c7c 100%)}
.hero-title{left:0;top:218px;width:1200px;text-align:center;color:var(--white);font-size:55px;font-weight:600}
.hero-sub{left:0;top:281px;width:1200px;text-align:center;color:var(--white);font-size:21px;font-weight:500;opacity:.95}
.btn-consult{left:488px;top:327px;width:224px;height:42px;background:var(--brand);border:1px solid #fff;border-radius:3px;color:var(--white);font-size:16px;display:flex;align-items:center;justify-content:center}
.slide-arrow{top:367px;width:36px;height:36px;border-radius:50%;background:rgba(255,255,255,.45)}

/* about */
.portrait{left:160px;top:731px;width:248px;height:248px;border-radius:50%;background:radial-gradient(circle at 50% 45%,#c99c86 0%,#6b4b3f 55%,#5b6570 100%)}
.about-rule{left:449px;top:734px;width:2px;height:62px;background:#bbb}
.about-name{left:464px;top:733px;font-size:22px;color:#333}
.about-role{left:464px;top:760px;font-size:36px;color:var(--brand);font-weight:500}
.about-text{left:449px;width:592px;font-size:11.5px;line-height:20px;color:#666}

/* practice areas */
.practice{left:0;top:1035px;width:1200px;height:472px;background:linear-gradient(120deg,#1f5fae 0%,#0d57a8 40%,#2a68b2 70%,#104f98 100%);color:var(--white)}
.practice-title{left:0;top:1080px;width:1200px;text-align:center;font-size:36px;font-weight:400}
.practice-sub{left:0;top:1123px;width:1200px;text-align:center;font-size:16px}
.practice-divider{left:564px;top:1158px;width:72px;height:2px;background:var(--white)}
.area{width:230px;text-align:center;color:var(--white)}
.area svg{display:block;margin:0 auto}
.area h3{font-family:"Raleway",sans-serif;font-weight:500;font-size:16px;margin-top:36px}
.area p{font-size:11.5px;font-weight:700;line-height:21px;margin-top:8px}

/* blog */
.section-title{left:97px;top:1558px;font-size:23px;color:#222}
.section-title span{color:#1a8ad4}
.post-thumb{left:98px;width:172px;height:139px;background:linear-gradient(135deg,#d9dde3,#5a6070 60%,#2c3140)}
.post-title{left:293px;font-size:14px;color:#222}
.post-meta{left:293px;font-size:10.5px;color:var(--brand)}
.post-text{left:293px;width:450px;font-size:11.5px;line-height:22px;color:#555}
.post-rule{left:293px;width:347px;height:1px;background:var(--line)}

/* quote form */
.quote{left:840px;top:1564px;width:260px;height:351px;background:var(--panel)}
.quote-head{left:840px;top:1564px;width:260px;height:46px;background:var(--brand-soft);color:var(--white);font-size:17px;display:flex;align-items:center;justify-content:center;letter-spacing:.5px}
.field{left:861px;width:218px;height:39px;background:var(--white);border:1px solid #eee;font-size:12px;color:#555;display:flex;align-items:center;gap:8px;padding-left:10px}
.btn-signup{left:861px;top:1849px;width:139px;height:38px;background:var(--brand-soft);border:2px solid #9db2d8;border-radius:3px;color:var(--white);font-size:13px;display:flex;align-items:center;justify-content:center}

/* footer */
.footer{left:0;top:1986px;width:1200px;height:229px;background:var(--brand);color:var(--white)}
.foot-h{top:2026px;font-size:17px;font-weight:500}
.foot-t{font-size:12px;line-height:20px}
.news-input{left:690px;top:2124px;width:165px;height:37px;background:var(--white);color:#999;font-size:11px;display:flex;align-items:center;padding-left:12px}
.news-btn{left:855px;top:2124px;width:80px;height:37px;background:#2b2b2b;color:var(--white);font-size:14px;display:flex;align-items:center;justify-content:center}
.social{left:997px;display:flex;align-items:center;gap:10px;font-size:14px}
.social i{width:26px;height:26px;border:1px solid var(--white);border-radius:50%;display:block}
.bottombar{left:0;top:2215px;width:1200px;height:52px;background:var(--bar);color:#ddd;font-size:13px;display:flex;align-items:center;justify-content:center}
</style>
</head>
<body>

<!-- top bar -->
<div class="abs topbar">
  <div class="abs item" style="left:97px">
    <svg width="11" height="11" viewBox="0 0 24 24"><path fill="#fff" d="M6.6 10.8a15 15 0 0 0 6.6 6.6l2.2-2.2c.3-.3.7-.4 1-.2 1.1.4 2.3.6 3.6.6.6 0 1 .4 1 1V20c0 .6-.4 1-1 1A17 17 0 0 1 3 4c0-.6.4-1 1-1h3.5c.6 0 1 .4 1 1 0 1.3.2 2.5.6 3.6.1.3 0 .7-.2 1z"/></svg>
    <span>+1.555.010.4821</span>
  </div>
  <div class="abs item" style="left:267px">
    <svg width="12" height="10" viewBox="0 0 24 18"><rect x="1" y="1" width="22" height="16" fill="none" stroke="#fff" stroke-width="2"/><path d="M1 1l11 9 11-9" fill="none" stroke="#fff" stroke-width="2"/></svg>
    <span>info@benavideskurtzlaw.com</span>
  </div>
  <i class="abs sq" style="left:1052px"></i>
  <i class="abs sq" style="left:1073px"></i>
  <i class="abs sq" style="left:1089px"></i>
</div>

<!-- header -->
<header class="abs header">
  <div class="abs brand-name"><span class="l1">BENAVIDES</span><span class="l2">Kurtz Law</span></div>
  <nav class="nav">
    <a class="active" style="left:388px">HOME</a>
    <a style="left:464px">ABOUT LORETA BENAVIDES</a>
    <a style="left:669px">PRACTICE AREAS</a>
    <a style="left:817px">NEWS</a>
    <a style="left:897px">CONTACT</a>
  </nav>
  <div class="abs lang"><i class="flag"></i>ENGLISH<svg style="margin-left:22px" width="9" height="6" viewBox="0 0 9 6"><path d="M1 1l3.5 3.5L8 1" fill="none" stroke="#888"/></svg></div>
</header>

<!-- hero -->
<section class="abs hero" role="img" aria-label="Photograph of a waterfront city skyline at dusk"></section>
<h1 class="abs head hero-title">Criminal Defence Law</h1>
<p class="abs head hero-sub">Nemo enim ipsam voluptatem quia voluptas</p>
<a class="abs btn-consult">Get Your Free Consultation</a>
<div class="abs slide-arrow" style="left:54px"><svg width="36" height="36"><path d="M20 12l-6 6 6 6" fill="none" stroke="#fff" stroke-width="2"/></svg></div>
<div class="abs slide-arrow" style="left:1116px"><svg width="36" height="36"><path d="M16 12l6 6-6 6" fill="none" stroke="#fff" stroke-width="2"/></svg></div>

<!-- about -->
<div class="abs portrait" role="img" aria-label="Portrait photograph of attorney Loreta Benavides-Kurtz"></div>
<div class="abs about-rule"></div>
<p class="abs head about-name">Loreta Benavides-Kurtz</p>
<h2 class="abs head about-role">&amp; I'm a Sole Practitioner</h2>
<p class="abs about-text" style="top:816px">Lorem ipsum dolor sit amet, consectetur adipiscing elit, sed do eiusmod tempor incididunt ut labore et dolore magna aliqua. Ut enim ad minim veniam, quis nostrud exercitation ullamco laboris nisi ut aliquip ex ea commodo consequat. Duis aute irure dolor in reprehenderit in voluptate velit esse cillum</p>
<p class="abs about-text" style="top:884px">Sed ut perspiciatis unde omnis iste natus error sit voluptatem accusantium doloremque laudantium, totam rem aperiam, eaque ipsa quae ab illo inventore veritatis et quasi architecto beatae vitae dicta sunt explicabo. Nemo enim ipsam voluptatem quia voluptas sit aspernatur aut odit aut fugit, sed quia consequuntur magni dolores eos qui ratione voluptatem sequi nesciunt. Neque porro quisquam est, qui dolorem</p>

<!-- practice areas -->
<section class="abs practice" role="img" aria-label="Blue-tinted photograph of lawyers meeting with a client"></section>
<h2 class="abs head practice-title">Practice Areas</h2>
<p class="abs head practice-sub">Nemo enim ipsam voluptatem quia voluptas</p>
<div class="abs practice-divider"></div>
<svg class="abs" style="left:38px;top:1229px" width="30" height="56"><path d="M28 2L3 28l25 26" fill="none" stroke="#fff" stroke-width="1.5"/></svg>
<svg class="abs" style="left:1141px;top:1229px" width="30" height="56"><path d="M2 2l25 26L2 54" fill="none" stroke="#fff" stroke-width="1.5"/></svg>

<div class="abs area" style="left:80px;top:1205px">
  <svg width="106" height="106" viewBox="0 0 106 106"><circle cx="53" cy="53" r="51" fill="none" stroke="#fff" stroke-width="2"/>
    <g fill="#fff"><ellipse cx="53" cy="42" rx="5" ry="20"/><ellipse cx="53" cy="42" rx="4" ry="17" transform="rotate(-45 53 58)"/><ellipse cx="53" cy="42" rx="4" ry="17" transform="rotate(45 53 58)"/><ellipse cx="53" cy="46" rx="3" ry="12" transform="rotate(-85 53 58)"/><ellipse cx="53" cy="46" rx="3" ry="12" transform="rotate(85 53 58)"/><rect x="52" y="58" width="2" height="12"/></g></svg>
  <h3>DRUG POSSESSION</h3>
  <p>Pellentesque et lacus pretium tinunt. Pellentesque at metus. Donec nisl a nisl. Vestibulum ante</p>
</div>
<div class="abs area" style="left:344px;top:1205px">
  <svg width="106" height="106" viewBox="0 0 106 106"><circle cx="53" cy="53" r="51" fill="none" stroke="#fff" stroke-width="2"/>
    <circle cx="49" cy="49" r="14" fill="#fff"/><circle cx="49" cy="49" r="7" fill="#1d5dab"/><path d="M59 59l12 12" stroke="#fff" stroke-width="7" stroke-linecap="round"/></svg>
  <h3>FRAUD OFFENSES</h3>
  <p>Pellentesque et lacus pretium tinunt. Pellentesque at metus. Donec nisl a nisl. Vestibulum ante</p>
</div>
<div class="abs area" style="left:619px;top:1205px">
  <svg width="106" height="106" viewBox="0 0 106 106"><circle cx="53" cy="53" r="51" fill="none" stroke="#fff" stroke-width="2"/>
    <rect x="42" y="26" width="22" height="50" rx="8" fill="#fff"/><g fill="#1d5dab"><circle cx="53" cy="38" r="5"/><circle cx="53" cy="51" r="5"/><circle cx="53" cy="64" r="5"/></g><rect x="51" y="76" width="4" height="6" fill="#fff"/></svg>
  <h3>TRAFFIC OFFENSES</h3>
  <p>Pellentesque et lacus pretium tinunt. Pellentesque at metus. Donec nisl a nisl. Vestibulum ante</p>
</div>
<div class="abs area" style="left:884px;top:1205px">
  <svg width="106" height="106" viewBox="0 0 106 106"><circle cx="53" cy="53" r="51" fill="none" stroke="#fff" stroke-width="2"/>
    <g fill="#fff"><circle cx="40" cy="31" r="6"/><circle cx="66" cy="31" r="6"/></g>
    <g stroke="#fff" stroke-width="6" stroke-linecap="round" fill="none"><path d="M40 40v18M40 58l-7 16M40 58l6 16M40 45l14 -4M66 40v18M66 58l-6 16M66 58l7 16M66 45l-8 8"/></g></svg>
  <h3>DOMESTIC VIOLENCE</h3>
  <p>Pellentesque et lacus pretium tinunt. Pellentesque at metus. Donec nisl a nisl. Vestibulum ante</p>
</div>

<!-- latest blog -->
<h2 class="abs head section-title">LATEST <span>BLOG</span></h2>

<div class="abs post-thumb" style="top:1611px" role="img" aria-label="Photograph of business people signing documents at a table"></div>
<h3 class="abs head post-title" style="top:1606px">Nemo Enim Ipsam Voluptatem</h3>
<p class="abs post-meta" style="top:1637px">3 MINUTES AGO &nbsp; / &nbsp; 0 COMMENTS</p>
<p class="abs post-text" style="top:1662px">Lorem ipsum dolor sit amet, consectetur adipiscing elit, sed do eiusmod tempor incididunt ut labore et dolore magna aliqua. Ut enim ad minim veniam, quis nostrud exercitation ullamco laboris nisi ut aliquip ex ea commodo</p>
<div class="abs post-rule" style="top:1753px"></div>

<div class="abs post-thumb" style="top:1782px" role="img" aria-label="Photograph of a team of lawyers in suits"></div>
<h3 class="abs head post-title" style="top:1777px">Nemo Enim Ipsam Voluptatem</h3>
<p class="abs post-meta" style="top:1808px">3 MINUTES AGO &nbsp; / &nbsp; 0 COMMENTS</p>
<p class="abs post-text" style="top:1833px">Lorem ipsum dolor sit amet, consectetur adipiscing elit, sed do eiusmod tempor incididunt ut labore et dolore magna aliqua. Ut enim ad minim veniam, quis nostrud exercitation ullamco laboris nisi ut aliquip ex ea commodo</p>
<div class="abs post-rule" style="top:1924px"></div>

<!-- request a quote -->
<div class="abs quote"></div>
<div class="abs head quote-head">REQUEST A QUOTE</div>
<div class="abs field" style="top:1632px"><svg width="10" height="11" viewBox="0 0 10 11"><circle cx="5" cy="3" r="2.5" fill="#999"/><path d="M0 11a5 5 0 0 1 10 0z" fill="#999"/></svg>Your Name</div>
<div class="abs field" style="top:1683px"><svg width="11" height="9" viewBox="0 0 24 18"><rect x="1" y="1" width="22" height="16" fill="none" stroke="#999" stroke-width="2"/><path d="M1 1l11 9 11-9" fill="none" stroke="#999" stroke-width="2"/></svg>E -mail</div>
<div class="abs field" style="top:1734px"><svg width="10" height="10" viewBox="0 0 24 24"><path fill="#999" d="M6.6 10.8a15 15 0 0 0 6.6 6.6l2.2-2.2c.3-.3.7-.4 1-.2 1.1.4 2.3.6 3.6.6.6 0 1 .4 1 1V20c0 .6-.4 1-1 1A17 17 0 0 1 3 4c0-.6.4-1 1-1h3.5c.6 0 1 .4 1 1 0 1.3.2 2.5.6 3.6.1.3 0 .7-.2 1z"/></svg>Phone No</div>
<div class="abs field" style="top:1785px"><svg width="9" height="11" viewBox="0 0 9 11"><rect x=".5" y=".5" width="8" height="10" fill="none" stroke="#999"/><path d="M2 3h5M2 5.5h5M2 8h5" stroke="#999"/></svg>Subjects</div>
<a class="abs btn-signup">SIGN UP NOW</a>

<!-- footer -->
<footer class="abs footer"></footer>
<h4 class="abs head foot-h" style="left:97px">CONTACT US</h4>
<p class="abs foot-t" style="left:99px;top:2066px;font-size:13px">Loreta Benavides-Kurtz<br>Lakeview, FL 33012 USA</p>
<div class="abs" style="left:99px;top:2118px;display:flex;align-items:center;gap:16px;color:#fff;font-size:17px">
  <svg width="18" height="18" viewBox="0 0 24 24"><path fill="none" stroke="#fff" stroke-width="1.5" d="M6.6 10.8a15 15 0 0 0 6.6 6.6l2.2-2.2c.3-.3.7-.4 1-.2 1.1.4 2.3.6 3.6.6.6 0 1 .4 1 1V20c0 .6-.4 1-1 1A17 17 0 0 1 3 4c0-.6.4-1 1-1h3.5c.6 0 1 .4 1 1 0 1.3.2 2.5.6 3.6.1.3 0 .7-.2 1z"/></svg>(+555) 014-2290</div>
<div class="abs" style="left:99px;top:2148px;display:flex;align-items:center;gap:16px;color:#fff;font-size:13px">
  <svg width="18" height="12" viewBox="0 0 24 18"><rect x="1" y="1" width="22" height="16" fill="none" stroke="#fff" stroke-width="1.5"/><path d="M1 1l11 9 11-9" fill="none" stroke="#fff" stroke-width="1.5"/></svg>info@benavideskurtzlaw.com</div>

<h4 class="abs head foot-h" style="left:390px">LATEST TWEET'S</h4>
<svg class="abs" style="left:392px;top:2074px" width="18" height="18"><rect width="18" height="18" rx="3" fill="#fff"/></svg>
<p class="abs foot-t" style="left:426px;top:2068px;width:205px;font-size:11.5px">Phasellus porta. Fusce susct varius mi. Cum sociis natoque penabus et magnis dis parturient montes, nasce-tur ridiculus mus. See more here ttp://t.co/Q4Rkzm2LpX</p>

<h4 class="abs head foot-h" style="left:688px">SIGN UP FOR NEWSLETTER</h4>
<p class="abs foot-t" style="left:688px;top:2066px;width:260px;font-size:11.5px">Excepteur sint occaecat cupidatat non proident, sunt in culpa qui officia deserunt mollit anim</p>
<div class="abs news-input">Enter your email address</div>
<div class="abs news-btn">Sign Up</div>

<h4 class="abs head foot-h" style="left:997px">SOCIAL MEDIA</h4>
<div class="abs social" style="top:2072px"><i></i>Facepage</div>
<div class="abs social" style="top:2108px"><i></i>Chirper</div>
<div class="abs social" style="top:2144px"><i></i>Circles+</div>

<div class="abs bottombar">2016 &nbsp;All Rights Reserved. Loreta Benavides-Kurtz</div>

</body>
</html>
```